Brightfield Optics seeks updated contemporary business card

Brightfield Optics utilizes advanced technology and we take pride in the modern look and feel of our practice. We like our current card, but it's been four years so it is time for an update.

Target Market(s)

Females 25-45 make the most health care decisions for their family.

Contact Information for Business Card

Clean front. Back with info and with empty space for appointment time or other small note

Requirements
Must have
• Logo
Ridge Marketvale, 28413 E Larkspur Ave
Cedar Terrace Marketvale, 4638 S Dunmore Rd
Call or text: 509-342-1968
email: hello@brightfieldoptics.example
brightfieldoptics.example
Dr Tobias Werring & Associates

```html
<!DOCTYPE html>
<html lang="en">
<head>
<meta charset="utf-8">
<title>Brightfield Optics – Business Card</title>
<link href="https://fonts.googleapis.com/css2?family=Exo+2:wght@500;700&display=swap" rel="stylesheet">
<style>
  :root {
    --backdrop: #3a3a3c;
    --navy: #1d2a5c;
    --deep-blue: #2c5a93;
    --mid-blue: #1e88cc;
    --sky-blue: #1ea6e4;
    --accent-text: #1ea6e4;
    --rule-grey: #c9ccd1;
    --paper: #ffffff;
  }
  * { box-sizing: border-box; margin: 0; padding: 0; }
  html, body {
    width: 1200px; height: 900px; overflow: hidden;
    background: var(--backdrop);
    font-family: "Exo 2", sans-serif;
  }
  .stage {
    width: 1200px; height: 900px;
    display: flex; align-items: center; justify-content: center; gap: 50px;
  }
  .card {
    position: relative;
    width: 525px; height: 300px;
    border-radius: 20px;
    overflow: hidden;
    background: var(--paper);
  }
  /* Front */
  .card-front .top-panel {
    position: absolute; inset: 0 0 auto 0; height: 190px;
    background: linear-gradient(160deg, var(--deep-blue) 0%, var(--mid-blue) 60%, var(--sky-blue) 100%);
  }
  .card-front .bottom-strip {
    position: absolute; left: 0; right: 0; bottom: 0; height: 22px;
    background: linear-gradient(90deg, var(--mid-blue), var(--sky-blue));
  }
  .card-front .brand-name {
    position: absolute; left: 0; right: 0; top: 78px;
    text-align: center;
    color: var(--paper);
    font-weight: 700; font-size: 40px; letter-spacing: 1px;
    text-transform: uppercase;
  }
  /* Back */
  .card-back .band { position: absolute; inset: 0; }
  .card-back .brand-name {
    position: absolute; right: 26px; top: 58px;
    color: var(--navy);
    font-weight: 700; font-size: 27px; letter-spacing: 0.5px;
    text-transform: uppercase;
  }
  .card-back .doctor-name {
    position: absolute; left: 24px; top: 150px;
    color: var(--accent-text);
    font-weight: 700; font-size: 21px; line-height: 1.1;
    text-transform: uppercase;
  }
  .contact-list {
    position: absolute; left: 258px; top: 160px;
    list-style: none;
    color: var(--paper);
    font-weight: 500; font-size: 11.5px; line-height: 1.35;
  }
  .contact-list li { display: flex; align-items: flex-start; gap: 8px; margin-bottom: 3px; }
  .contact-list svg { flex: none; width: 13px; height: 13px; margin-top: 1px; }
</style>
</head>
<body>
<main class="stage">

  <section class="card card-front" aria-label="Card front">
    <div class="top-panel"></div>
    <div class="brand-name">Brightfield Optics</div>
    <div class="bottom-strip"></div>
  </section>

  <section class="card card-back" aria-label="Card back">
    <svg class="band" viewBox="0 0 525 300" preserveAspectRatio="none" aria-hidden="true">
      <defs>
        <linearGradient id="backBlue" x1="0" y1="0" x2="1" y2="1">
          <stop offset="0" stop-color="#1e88cc"/>
          <stop offset="1" stop-color="#1ea6e4"/>
        </linearGradient>
      </defs>
      <polygon points="0,212 240,212 240,143 525,143 525,149 246,149 246,218 0,218" fill="#c9ccd1"/>
      <polygon points="0,218 246,218 246,149 525,149 525,300 0,300" fill="url(#backBlue)"/>
    </svg>

    <div class="brand-name">Brightfield Optics</div>

    <div class="doctor-name">Dr. Tobias Werring<br>&amp; Associates</div>

    <ul class="contact-list">
      <li>
        <svg viewBox="0 0 24 24" aria-hidden="true"><path fill="#fff" d="M12 2a7 7 0 0 0-7 7c0 5 7 13 7 13s7-8 7-13a7 7 0 0 0-7-7zm0 9.5A2.5 2.5 0 1 1 12 6.5a2.5 2.5 0 0 1 0 5z"/></svg>
        <span>Ridge Marketvale, 28413 E Larkspur Ave<br>Cedar Terrace Marketvale, 4638 S Dunmore Rd</span>
      </li>
      <li>
        <svg viewBox="0 0 24 24" aria-hidden="true"><path fill="#fff" d="M6.6 10.8a15 15 0 0 0 6.6 6.6l2.2-2.2a1 1 0 0 1 1-.25 11.4 11.4 0 0 0 3.6.6 1 1 0 0 1 1 1V20a1 1 0 0 1-1 1A17 17 0 0 1 3 4a1 1 0 0 1 1-1h3.5a1 1 0 0 1 1 1c0 1.25.2 2.45.6 3.6a1 1 0 0 1-.25 1z"/></svg>
        <span>509-342-1968</span>
      </li>
      <li>
        <svg viewBox="0 0 24 24" aria-hidden="true"><path fill="#fff" d="M3 5h18v14H3zm2 2v.5l7 4.5 7-4.5V7l-7 4.5z"/></svg>
        <span>hello@brightfieldoptics.example</span>
      </li>
      <li>
        <svg viewBox="0 0 24 24" aria-hidden="true"><circle cx="12" cy="12" r="9" fill="none" stroke="#fff" stroke-width="2"/><path d="M3 12h18M12 3c3 3 3 15 0 18M12 3c-3 3-3 15 0 18" fill="none" stroke="#fff" stroke-width="1.5"/></svg>
        <span>brightfieldoptics.example</span>
      </li>
    </ul>
  </section>

</main>
</body>
</html>
```